Business card design needed

Want the logo on a medium blue background and a nice funky design. I have my own gym and run one on one personal training and nutrition sessions. want it to look lively.
Updates

Please note I requested my logo on a blue background 

PLEASE NOTE: I already have a logo. It is attached to the order!!

Target Market(s)

over 55s

Industry/Entity Type

Nutrition

Contact Information for Business Card

Front of card : Logo ( on blue background )
Keldra Ashby
Nutrition & Fitness Coach for Seniors
Private gym at : 17 Tindal Crescent, Wembury, Perth, WA 6166
Mob : 0418372651
Email : keldraashby@frelmo.com
"For Seniors by a Senior"

Back of card
B.A. ( Soc.)
Dip. Ed. (Sec.)
Wellness Coach
Cert 4 Personal Trainer
Cert. Nutritition
MOVE ON Facilitator
Ageing Boldly Moving Freely Facilitator
NLP Master

```html
<!DOCTYPE html>
<html lang="en">
<head>
<meta charset="utf-8">
<title>Keldra Ashby – Credentials Card</title>
<link rel="stylesheet" href="https://fonts.googleapis.com/css2?family=Carlito:wght@400;700&display=swap">
<style>
  :root {
    --blue-core: #1a5fc4;
    --blue-mid: #0f4aa6;
    --blue-deep: #072a6e;
    --blue-edge: #041d52;
    --sky: #3fa6de;
    --text: #f2f6fc;
    --rule-light: #e6ecf5;
    --rule-shadow: rgba(0, 10, 40, 0.55);
  }
  html, body {
    margin: 0;
    padding: 0;
    width: 1200px;
    height: 692px;
    overflow: hidden;
    background: var(--blue-edge);
  }
  .card {
    position: relative;
    width: 1200px;
    height: 692px;
    overflow: hidden;
    font-family: "Carlito", "Calibri", Arial, sans-serif;
    color: var(--text);
    background:
      radial-gradient(ellipse 70% 75% at 50% 18%, var(--blue-core) 0%, var(--blue-mid) 45%, var(--blue-deep) 85%, var(--blue-edge) 100%);
  }
  .card::before,
  .card::after {
    content: "";
    position: absolute;
    top: 0;
    bottom: 0;
    width: 90px;
    pointer-events: none;
  }
  .card::before { left: 0; background: linear-gradient(90deg, rgba(2, 16, 50, 0.55), rgba(2, 16, 50, 0)); }
  .card::after { right: 0; background: linear-gradient(270deg, rgba(2, 16, 50, 0.55), rgba(2, 16, 50, 0)); }

  .brand {
    position: absolute;
    top: 166px;
    left: 0;
    right: 0;
    display: flex;
    justify-content: center;
    align-items: center;
    gap: 12px;
  }
  .brand-dot {
    width: 26px;
    height: 26px;
    border-radius: 50%;
    background: var(--sky);
  }
  .brand-name {
    font-size: 40px;
    font-weight: 400;
    color: var(--sky);
    letter-spacing: 0.5px;
    line-height: 1;
  }

  .credentials {
    position: absolute;
    left: 0;
    right: 0;
    margin: 0;
    text-align: center;
    font-size: 22px;
    font-weight: 400;
    line-height: 1;
  }
  .credentials-top { top: 291px; }
  .credentials-bottom { top: 379px; }

  .divider {
    position: absolute;
    top: 345px;
    left: 155px;
    width: 878px;
    height: 2px;
    background: linear-gradient(90deg, rgba(230, 236, 245, 0.75), var(--rule-light) 12%, var(--rule-light) 88%, rgba(230, 236, 245, 0.75));
    box-shadow: 0 2px 2px var(--rule-shadow);
  }
</style>
</head>
<body>
  <main class="card">
    <div class="brand">
      <span class="brand-dot"></span>
      <span class="brand-name">Ashby Active</span>
    </div>

    <p class="credentials credentials-top">B.A. ( Soc.), Dip. Ed. (Sec.), Cert 4 Personal Trainer, Wellness Coach,</p>
    <div class="divider"></div>
    <p class="credentials credentials-bottom">MOVE ON Facilitator, Ageing Boldly Moving Freely facilitator, NLP Master.</p>
  </main>
</body>
</html>
```